Poster Design Project

Need a design for a music festival called Contra-Lindenfest

The design needs to have areas for the following:
- Band Names
- DJ Names
- Sponsor Names and Logos
- Event location, Date & Time

Industry/Entity Type

Festival

```html
<!DOCTYPE html>
<html lang="en">
<head>
<meta charset="utf-8">
<title>Contra-Lindenfest</title>
<link rel="stylesheet" href="https://fonts.googleapis.com/css2?family=Fredoka:wght@700&family=Titan+One&display=swap">
<style>
  :root {
    --sky-top: #5cc2ef;
    --sky-mid: #a9dcf3;
    --sky-haze: #cfeaf4;
    --stage-blue: #7fb0c9;
    --stage-deep: #3d6a82;
    --night: #000000;
    --festival-orange: #f7a53b;
    --outline: #3a2a12;
    --paper: #ffffff;
    --cloud: #eef8fc;
    --charity-navy: #1d2f6b;
  }
  * { margin: 0; padding: 0; box-sizing: border-box; }
  html, body { width: 849px; height: 1200px; overflow: hidden; background: var(--night); }
  .poster {
    position: relative;
    width: 849px;
    height: 1200px;
    overflow: hidden;
    font-family: "Titan One", sans-serif;
    color: var(--festival-orange);
  }
  .poster__sky {
    position: absolute;
    inset: 0 0 auto 0;
    height: 640px;
    background: linear-gradient(180deg, var(--sky-top) 0%, var(--sky-mid) 45%, var(--sky-haze) 100%);
  }
  .poster__crowd {
    position: absolute;
    top: 600px;
    left: 0;
    width: 100%;
    height: 330px;
    background: linear-gradient(180deg,
      var(--sky-haze) 0%,
      var(--stage-blue) 22%,
      var(--stage-deep) 48%,
      #14232b 68%,
      var(--night) 86%);
  }
  .poster__night {
    position: absolute;
    top: 930px;
    left: 0;
    width: 100%;
    bottom: 0;
    background: var(--night);
  }
  .poster__title {
    position: absolute;
    top: 0;
    left: 0;
    width: 100%;
    text-align: center;
    font-family: "Fredoka", sans-serif;
    font-weight: 700;
    font-size: 86px;
    line-height: 96px;
    letter-spacing: 2px;
    -webkit-text-stroke: 2px var(--outline);
    paint-order: stroke fill;
  }
  .poster__supporting {
    position: absolute;
    top: 96px;
    left: 435px;
    font-size: 23px;
    letter-spacing: 2px;
  }
  .beneficiary {
    position: absolute;
    top: 100px;
    left: 590px;
    width: 192px;
    height: 140px;
    padding: 14px 0 0 18px;
    border-radius: 60px;
    background: var(--cloud);
    color: var(--charity-navy);
  }
  .beneficiary__name {
    display: flex;
    align-items: center;
    gap: 8px;
    font-size: 22px;
    line-height: 28px;
  }
  .beneficiary__mark {
    flex: none;
    width: 18px;
    height: 18px;
    background: var(--charity-navy);
  }
  .beneficiary__tagline {
    display: block;
    margin-top: 6px;
    font-size: 11px;
    letter-spacing: 1px;
  }
  .lineup {
    position: absolute;
    top: 154px;
    left: 37px;
  }
  .lineup__label {
    font-size: 21px;
    letter-spacing: 1px;
    margin-bottom: 2px;
  }
  .lineup__acts { list-style: none; }
  .lineup__act {
    font-size: 44px;
    line-height: 58.3px;
    letter-spacing: 2px;
  }
  .event-details {
    position: absolute;
    top: 908px;
    left: 20px;
  }
  .event-details__date {
    font-size: 70px;
    line-height: 80px;
    letter-spacing: 2px;
    margin-left: 17px;
  }
  .event-details__time {
    font-size: 26px;
    margin-top: 2px;
    letter-spacing: 1px;
  }
  .event-details__address {
    font-size: 27px;
    margin-top: 6px;
    letter-spacing: 1px;
  }
  .sponsors {
    position: absolute;
    bottom: 22px;
    right: 20px;
    display: flex;
    align-items: center;
    gap: 26px;
    font-size: 17px;
    color: var(--paper);
  }
  .sponsors__item { display: flex; align-items: center; gap: 8px; }
  .sponsors__mark {
    width: 14px;
    height: 14px;
    border-radius: 50%;
    background: var(--paper);
  }
</style>
</head>
<body>
<main class="poster">
  <div class="poster__sky" role="img" aria-label="Bright blue sky with soft white clouds"></div>
  <div class="poster__crowd" role="img" aria-label="Silhouetted band playing on stage above a cheering crowd with raised hands"></div>
  <div class="poster__night"></div>

  <h1 class="poster__title">Contra-Lindenfest</h1>
  <p class="poster__supporting">supporting</p>
  <div class="beneficiary">
    <span class="beneficiary__name"><span class="beneficiary__mark"></span>Restful Nights</span>
    <span class="beneficiary__tagline">SLEEP SOUND TONIGHT</span>
  </div>

  <section class="lineup">
    <p class="lineup__label">Featuring</p>
    <ul class="lineup__acts">
      <li class="lineup__act">Small Borough</li>
      <li class="lineup__act">Odd Chemistry</li>
      <li class="lineup__act">Hale &amp; Wyeth Company</li>
      <li class="lineup__act">The GreyWolves</li>
      <li class="lineup__act">Nora Bennett</li>
      <li class="lineup__act">Groovy Fellow</li>
      <li class="lineup__act">Moth Lantern</li>
      <li class="lineup__act">The Proven</li>
    </ul>
  </section>

  <section class="event-details">
    <p class="event-details__date">September 15th</p>
    <p class="event-details__time">11:00A - Until</p>
    <p class="event-details__address">512 W. 28th St, Fairbrook, NC 28999</p>
  </section>

  <footer class="sponsors">
    <span class="sponsors__item"><span class="sponsors__mark"></span>Crowdline</span>
    <span class="sponsors__item">Wrenhill Brewing</span>
    <span class="sponsors__item">Eastmill Brewing</span>
  </footer>
</main>
</body>
</html>
```